TotsyPlum Business needs a Box Design

We need a box design for a new product Teething Mittens. Please check our file for a demo and Layout, Box mockup, Logo Vector
https://files.sharevault-example.com/folders/8kQzLmW3pXrT7nVb2YcHd4JfGs9Ne6Ua

Target Market(s)

A parent have baby 6 - 12 month

Industry/Entity Type

Baby

Font styles to use
Decorative
Script

Requirements
Must have
• Our logo in a Box and follow our guide
Nice to have
• Cute design

```html
<!DOCTYPE html>
<html lang="en">
<head>
<meta charset="utf-8">
<title>TotsyPlum Teething Mitten Box Dieline</title>
<link rel="stylesheet" href="https://fonts.googleapis.com/css2?family=Dancing+Script:wght@600&family=Open+Sans:wght@400&family=Oswald:wght@300;400&display=block">
<style>
  :root {
    --mint: #d7ebe2;
    --line: #2f2f2f;
    --panel: #ffffff;
    --gold: #e2c074;
    --ink: #3a3a3a;
    --pattern-cream: #fbf0c4;
    --pattern-mint: #d9efe4;
    --pattern-pink: #f9dfe4;
    --page: #ffffff;
  }
  html, body {
    margin: 0;
    padding: 0;
    width: 1200px;
    height: 1121px;
    overflow: hidden;
    background: var(--page);
  }
  .dieline {
    display: block;
    width: 1200px;
    height: 1121px;
  }
  .flap { fill: var(--mint); stroke: var(--line); stroke-width: 0.8; }
  .panel { fill: var(--panel); stroke: var(--line); stroke-width: 0.8; }
  .fold { stroke: var(--line); stroke-width: 0.8; fill: none; }
  .hang-slot { fill: #ffffff; stroke: var(--line); stroke-width: 0.8; }
  .pattern-area { fill: url(#softPattern); }
  .window { fill: #ffffff; stroke: var(--line); stroke-width: 0.8; }
  .brand-dot { fill: var(--gold); }
  .brand-name {
    font-family: "Open Sans", sans-serif;
    font-weight: 400;
    font-size: 15px;
    fill: var(--gold);
  }
  .product-name {
    font-family: "Dancing Script", cursive;
    font-weight: 600;
    font-size: 24px;
    fill: var(--gold);
  }
  .instructions {
    font-family: "Oswald", sans-serif;
    font-weight: 300;
    font-size: 8.2px;
    fill: var(--ink);
  }
</style>
</head>
<body>
<svg class="dieline" viewBox="0 0 850 794" xmlns="http://www.w3.org/2000/svg">
  <defs>
    <linearGradient id="softPattern" x1="0" y1="0" x2="1" y2="1">
      <stop offset="0" stop-color="#fbf0c4"/>
      <stop offset="0.5" stop-color="#d9efe4"/>
      <stop offset="1" stop-color="#f9dfe4"/>
    </linearGradient>
  </defs>

  <g class="back-panel">
    <rect class="flap" x="20" y="28" width="284" height="185"/>
    <line class="fold" x1="20" y1="128" x2="304" y2="128"/>
    <rect class="hang-slot" x="143" y="108" width="40" height="10" rx="5"/>
    <rect class="hang-slot" x="143" y="137" width="40" height="10" rx="5"/>
    <rect class="panel" x="20" y="213" width="284" height="454"/>
    <path class="flap" d="M20 667 H304 V780 Q304 795 289 795 H35 Q20 795 20 780 Z"/>
    <line class="fold" x1="20" y1="750" x2="304" y2="750"/>

    <circle class="brand-dot" cx="162" cy="248" r="13"/>
    <text class="brand-name" x="162" y="289" text-anchor="middle">TotsyPlum</text>

    <text class="instructions" x="68" y="327">
      <tspan x="68" y="327">Instructions</tspan>
      <tspan x="68" y="349">Mid-decade data reveal rapid growth in the</tspan>
      <tspan x="68" y="360">U.S. English learner population.6</tspan>
      <tspan x="68" y="371"> During</tspan>
      <tspan x="68" y="382">the 2007–08 school year, English learners</tspan>
      <tspan x="68" y="392">represented 10.6 percent of the K–12 public</tspan>
      <tspan x="68" y="403">school enrollment, or more than 5.3 million</tspan>
      <tspan x="68" y="414">students.7</tspan>
      <tspan x="68" y="425"> In fact, English learners are the</tspan>
      <tspan x="68" y="436">fastest-growing segment of the student population,</tspan>
      <tspan x="68" y="447">with their growth highest in grades</tspan>
      <tspan x="68" y="458">seven through twelve.8</tspan>
      <tspan x="68" y="469"> Figures 1 and 2 show</tspan>
      <tspan x="68" y="480">the dramatic increases in English learner</tspan>
      <tspan x="68" y="490">populations, particularly in states that are</tspan>
      <tspan x="68" y="501">not accustomed to serving their instructional</tspan>
      <tspan x="68" y="512">needs. These students have lower academic</tspan>
      <tspan x="68" y="523">performance and lower graduation rates than</tspan>
      <tspan x="68" y="534">native white students and have affected the</tspan>
      <tspan x="68" y="545">nation’s overall educational attainment.9</tspan>
      <tspan x="68" y="556">About 79 percent of English learners in the</tspan>
      <tspan x="68" y="567">United States speak Spanish as their native</tspan>
      <tspan x="68" y="577">language; much lower shares speak Chinese,</tspan>
      <tspan x="68" y="588">Vietnamese, Hmong, and Korean.</tspan>
    </text>

    <text class="product-name" x="162" y="634" text-anchor="middle">Baby Mitten</text>
  </g>

  <g class="side-panel-left">
    <path class="flap" d="M304 213 V172 L317 146 H417 V213 Z"/>
    <rect class="panel" x="304" y="213" width="113" height="454"/>
    <rect class="pattern-area" x="305" y="214" width="111" height="452" role="img" aria-label="Cute pattern of smiling bees, butterflies and small flowers in yellow, mint and pink"/>
    <path class="flap" d="M304 667 H417 V785 H320 L304 700 Z"/>
  </g>

  <g class="front-panel">
    <path class="panel" d="M417 213 V101 Q417 86 432 86 H685 Q700 86 700 101 V213 Z"/>
    <path class="flap" d="M417 128 V101 Q417 86 432 86 H685 Q700 86 700 101 V128 Z"/>
    <rect class="pattern-area" x="418" y="129" width="281" height="83" role="img" aria-label="Cute pattern of smiling bees, butterflies and small flowers on the lid"/>
    <rect class="panel" x="417" y="213" width="283" height="454"/>
    <rect class="pattern-area" x="418" y="214" width="281" height="452" role="img" aria-label="Cute pattern of smiling bees, butterflies and small flowers framing the window"/>
    <path class="window" d="M472 288 H670 V590 H478 Q446 590 446 558 V314 Q446 288 472 288 Z"/>
    <circle class="brand-dot" cx="566" cy="236" r="12"/>
    <text class="brand-name" x="566" y="275" text-anchor="middle">TotsyPlum</text>
    <text class="product-name" x="565" y="634" text-anchor="middle">Baby Mitten</text>
    <path class="flap" d="M417 667 H700 V750 H417 Z"/>
  </g>

  <g class="side-panel-right">
    <path class="flap" d="M700 213 V146 H800 L813 172 V213 Z"/>
    <rect class="panel" x="700" y="213" width="113" height="454"/>
    <rect class="pattern-area" x="701" y="214" width="111" height="452" role="img" aria-label="Cute pattern of smiling bees, butterflies and small flowers in yellow, mint and pink"/>
    <path class="flap" d="M700 667 H813 V700 L797 785 H700 Z"/>
  </g>

  <path class="panel glue-flap" d="M813 213 L840 240 V640 L813 667 Z"/>
</svg>
</body>
</html>
```